Visualisation Software brochure

i need a sales brochure for a new visualisation software company called Lumora Scene Studio.
The software has been specifically designed for manufacturers, distributers and retailers in the design / décor / furnishing / building industries. It allows customers can then import unlimited numbers of digital photos of rooms from their own home or take advantage of a library of pre-made photos, and then render different products from your catalogue into that photo to see what the finished look will be.
i have attached:
1) a mock up of the home page of the website
2) example of brochure wording that i have put together (although i am a little unsure about what other words i can add - so any suggestions here would be good)
3) i have attached some examples of other brochures that i like and would like similar designs
I am after a classy brochure used by a large corporate technology company that is given to executives and gives an impression of quality, trustworthiness and innovation.
• the colour blue as per the colours on my website mock up provided in the design brief
• I like simple, smart, clean and uncluttered design
• I like simple, clean and uncluttered design
• I like pictures that fit in with my technology (whether that be home and interior design, mixing virtual world and real world, visualising an idea) rather than basic stock of corporate people
Updates
Target Market(s)
marketing professionals
Industry/Entity Type
Software
Font styles to use
Look and feel
Each slider illustrates characteristics of the customer's brand and the style your logo design should communicate.

```html
<!DOCTYPE html>
<html lang="en">
<head>
<meta charset="utf-8">
<title>Lumora Scene Studio – Brochure</title>
<link href="https://fonts.googleapis.com/css2?family=Arimo:wght@400;700&display=swap" rel="stylesheet">
<style>
:root{
  --page:#e4e4e4;
  --panel:#a7a7a7;
  --ink:#f4f4f4;
  --frame:#f7f7f7;
  --rule:#d2d2d2;
  --photo-room:#8f8c92;
  --photo-sofa:#3f7fc0;
  --photo-loft:#d9d3c8;
  --photo-lamp:#c9c9c9;
}
*{box-sizing:border-box;margin:0;padding:0}
html,body{width:1200px;height:1000px;overflow:hidden;background:var(--page)}
body{position:relative;font-family:"Arimo",Arial,sans-serif;color:var(--ink)}
.spread{position:absolute;left:28px;top:88px;width:1148px;height:812px;background:var(--panel)}
.spread-rule{position:absolute;left:28px;top:885px;width:1148px;height:1px;background:var(--rule)}
.photo{position:absolute}
.photo-frame{position:absolute;border:1px solid var(--frame)}
.photo-living{left:52px;top:113px;width:241px;height:310px;background:linear-gradient(180deg,#a4a2ab 0%,#8d8b93 65%,#55524f 100%)}
.photo-sofa-box{left:326px;top:121px;width:240px;height:137px;border:1px solid var(--frame)}
.photo-sofa{position:absolute;left:14px;top:12px;width:210px;height:112px;border-radius:10px;background:radial-gradient(ellipse at 50% 55%,var(--photo-sofa) 0%,#2f6aa6 45%,rgba(167,167,167,0) 72%)}
.photo-loft{left:624px;top:113px;width:530px;height:294px;background:linear-gradient(100deg,#e7e2da 0%,#cfc7ba 45%,#b9a893 60%,#e0e6dc 80%,#8fae6a 100%)}
.photo-lamp-box{left:916px;top:754px;width:94px;height:104px;border:1px solid #c4c4c4}
.photo-lamp{position:absolute;left:16px;top:8px;width:60px;height:86px;background:linear-gradient(180deg,#f2f2f2 0%,#d4d4d4 40%,#b6b6b6 100%);border-radius:4px}
.column{position:absolute;font-size:10.4px;line-height:12.6px}
.column h2{font-size:10.4px;font-weight:700;line-height:12.6px;margin-bottom:11px}
.column p{margin-bottom:13px}
.col-challenge{left:52px;top:456px;width:252px}
.col-solution{left:326px;top:268px;width:250px}
.col-retailer{left:625px;top:450px;width:230px}
.col-consumer{left:909px;top:452px;width:236px}
.brand{position:absolute;left:1022px;top:786px;display:flex;align-items:center;gap:6px}
.brand-dot{width:12px;height:12px;border-radius:50%;background:var(--ink)}
.brand-name{font-size:10.4px;font-weight:700;color:var(--ink);line-height:12px;width:90px}
</style>
</head>
<body>
<div class="spread"></div>
<div class="spread-rule"></div>

<div class="photo photo-living" role="img" aria-label="Modern living room with grey armchair and floor lamp">
  <div class="photo-frame" style="left:13px;top:9px;width:217px;height:286px"></div>
</div>

<div class="photo photo-sofa-box">
  <div class="photo-sofa" role="img" aria-label="Blue three-seat sofa with patterned cushions"></div>
</div>

<div class="photo photo-loft" role="img" aria-label="Bright open-plan lounge with bookshelves, orange sofa and garden view">
  <div class="photo-frame" style="left:16px;top:14px;width:508px;height:263px"></div>
</div>

<section class="column col-challenge">
  <h2>The challenge for both customers and retailers</h2>
  <p>Gone are the days when all you needed was a showroom, a product line, and a business card. Customers are better informed, more interactive, and more selective than ever before. With access to a range of new technologies and a wide variety of online resources, these connected consumers are increasingly demanding a dynamic, seamless, integrated, consistent, accessible and personalised experience with your brand across all online, bricks-and-mortar and mobile channels.</p>
  <p>The customer must be empowered to interact across all touchpoints and channels; they want to browse and buy on their own schedules and retailers must offer equally accurate and immediate access to products and customer service. Consumers want to be inspired and be given the tools, advice and confidence to create unique, personal spaces - meaning companies need to feed this design dream and appealing to their vision is essential. The shopping experience should be built around the new reality that most consumers make their browsing and purchasing commitments online, often before they ever see the product in person.</p>
  <p>Amid ongoing economic uncertainty, true omni-channel retailers need to continue to focus on understanding the customer psyche and leveraging innovation to drive loyalty and customer engagement and ultimately increase sales.</p>
</section>

<section class="column col-solution">
  <h2>The virtualised solution</h2>
  <p>Having your own branded virtual design software embedded on your website or accessible via an Nimbus and/or Aurel app will help bridge the gap between your customers’ design dreams and your products. Our software helps solve one of the biggest problems many experience whilst redecorating or designing their home, which is despite looking at numerous samples, most cannot visualise or conceptualise what the finished look will be.</p>
  <p>It doesn’t matter what business you’re in. Your customers will be able to visualise all possible product combinations for their new home – it just depends on your range. The software can easily handle ‘flat surface products’ including roofing, cladding, garage doors, windows and driveways/ pathways to interior products such as carpet, tiles, timber and laminate flooring, doors, art works, bench tops and splashbacks.<br>Importantly, our technology can also handle any product in 3D - whether it be furniture, lighting, floor rugs, curtains / blinds, wardrobes, household items, kitchen cabinets and bathroom fixtures. A truly unique feature allows customers to simply delete the existing item from their photo and replace it with another product from your catalogue without removing any item physically.</p>
  <p>Today’s consumer doesn’t just rely on technological gimmicks such as augmented reality or one in-store visit before making important investment decisions. With so much competition in the marketplace consumers are more driven than ever to shop around with the amount and quality of value-adding service the real deal breaker rather than price.</p>
  <p>It has become more about initiating the education of your customer versus waiting for them to ask for assistance. Using our technology can increase sales conversion rates as once customers have identified what products they would like to purchase they come to you as educated buyers, already having experienced a fantastic customer interaction with your brand.</p>
</section>

<section class="column col-retailer">
  <h2>Retailer Benefits:</h2>
  <p>Be the market innovator and leader by combining technology and a dynamic, seamless, integrated and consistent level of customer service across all online, bricks-and-mortar and mobile channels that delivers the big wow factor</p>
  <p>Extend your reach - don't limit your technology footprint by only using Aurel apps - our solution leverages and optimises all mobile devices and desktops (AuOS, Nimbus, Web). This equates to a larger watershed of customers and more sales</p>
  <p>Increase brand engagement as our bespoke and scalable visualisation application will help customers build a relationship with your company, brand, and products and then share that experience within their social circles</p>
  <p>Understand buyer behaviour by receiving real usage statistics to obtain valuable insight about your customers and conduct trend analysis to determine how your future strategies can further enhance your bottom-line</p>
  <p>Increased sales to further grow your business</p>
  <p>Maximise the exposure of your products by uploading your entire product catalogue into a visualisation software that makes them look real</p>
</section>

<section class="column col-consumer">
  <h2>Consumer Benefits:</h2>
  <p>Reduce your customer’s purchase anxiety as they will have the knowledge that the products they are choosing from your range are the right choice</p>
  <p>Greater flexibility in the way they shop by being open 24/7 and being able to engage with your brand when they want and how they want. Happier customers and hence more sales.<br>An easy-to-use interface along with guided help and tutorials for those less confident with technology</p>
  <p>Being able to make informed purchasing decisions as they can easily compare a large range of your products at the touch of a computer key</p>
  <p>Improved personalised buying experience by enabling customers to use photos of their own personal spaces and incorporate your products</p>
</section>

<div class="photo photo-lamp-box">
  <div class="photo-lamp" role="img" aria-label="White drum-shade table lamp on chrome stand"></div>
</div>

<div class="brand">
  <span class="brand-dot"></span>
  <span class="brand-name">Lumora Scene Studio</span>
</div>
</body>
</html>
```